We need a tri fold brochure for a new private investigator based in Modesto CA called Brenwick Inquiry Partners. We rely heavily on technology and bring a new level of efficiency to the investigative industry.

We primarily serve individual attorneys and law firms with pre and post litigation support. We bring a higher level of professionalism and technology to our clients and plan on raining the bar of service provider expectation.

Target Market(s)

Attorneys and legal support staff

Industry/Entity Type

Private Investigator

Requirements
Must have
• I must have my logo and contact information, must only use the colors of red, white and black
Nice to have
• I would like a very clean and simple design, these are going to attorneys and legal support staff who need to be able to look at and and understand the tri-fold quickly and easily, but look very up-scale and sophisticated

```html
<!DOCTYPE html>
<html lang="en">
<head>
<meta charset="utf-8">
<title>Brenwick Inquiry Partners – Tri-fold Brochure</title>
<link rel="stylesheet" href="https://fonts.googleapis.com/css2?family=Questrial&family=Open+Sans:wght@400;600&display=swap">
<style>
  :root {
    --red: #e3141f;
    --black: #141414;
    --white: #ffffff;
    --ink: #2b2b2b;
    --shade-pale: #ececec;
    --shade: #c4c4c4;
    --stage: #e6e6e6;
  }
  * { box-sizing: border-box; margin: 0; padding: 0; }
  html, body {
    width: 1200px; height: 801px; overflow: hidden;
    background: var(--stage);
    font-family: "Open Sans", Arial, sans-serif;
    color: var(--ink);
  }
  .canvas { position: relative; width: 1200px; height: 801px; }

  .spread {
    position: absolute; left: 40px; top: 96px;
    display: flex; width: 786px; height: 610px;
    box-shadow: 0 6px 20px rgba(0,0,0,.18);
  }
  .panel {
    position: relative; width: 262px; height: 610px;
    padding: 34px 20px 20px;
    background: linear-gradient(to bottom, var(--white) 58%, var(--shade-pale) 82%, var(--shade) 100%);
  }
  .panel + .panel { border-left: 1px solid #d9d9d9; }
  .panel--centre {
    background: linear-gradient(to bottom, var(--shade) 0%, var(--white) 22%, var(--white) 58%, var(--shade-pale) 82%, var(--shade) 100%);
  }
  .cover {
    position: absolute; left: 880px; top: 96px;
    width: 272px; height: 610px; padding: 34px 20px 20px;
    background: linear-gradient(to bottom, var(--white) 60%, var(--shade-pale) 84%, var(--shade) 100%);
    box-shadow: 0 6px 20px rgba(0,0,0,.18);
  }

  .section-title {
    font-family: "Questrial", Arial, sans-serif;
    background: var(--red); color: var(--white);
    border-top: 2px solid var(--black);
    font-size: 12px; letter-spacing: .6px; text-transform: uppercase;
    padding: 5px 10px; margin: 0 -20px 10px;
  }
  .section-text {
    font-size: 9.5px; line-height: 1.55; margin-bottom: 18px; text-align: justify;
  }
  .service-list { list-style: none; margin: -6px 0 18px; }
  .service-list li {
    font-size: 9.5px; line-height: 1.8; padding-left: 14px; position: relative;
  }
  .service-list li::before {
    content: ""; position: absolute; left: 2px; top: 6px;
    width: 5px; height: 5px; background: var(--red);
  }

  .brand {
    display: flex; align-items: center; gap: 10px;
    margin: 12px 0 34px;
  }
  .brand__mark { width: 14px; height: 14px; border-radius: 50%; background: var(--red); flex: none; }
  .brand__name {
    font-family: "Questrial", Arial, sans-serif;
    font-size: 19px; line-height: 1.1; color: var(--black); text-transform: uppercase; letter-spacing: .5px;
  }

  .contact {
    position: absolute; left: 20px; right: 20px; bottom: 22px;
    border-top: 2px solid var(--red); padding-top: 10px;
    list-style: none;
  }
  .contact li {
    display: flex; align-items: center; gap: 8px;
    font-size: 9.5px; line-height: 1.9; color: var(--black);
  }
  .contact svg { width: 10px; height: 10px; flex: none; fill: var(--red); }
</style>
</head>
<body>
<main class="canvas">

  <section class="spread" aria-label="Brochure inside spread">
    <article class="panel">
      <h2 class="section-title">Statements</h2>
      <p class="section-text">Taking statements is a critical skill. Our investigators locate and interview witnesses with care, record accurate accounts, and deliver clear written summaries that hold up when your case moves forward to deposition or trial review.</p>
      <h2 class="section-title">Legal Testimony</h2>
      <p class="section-text">Our investigators prepare thoroughly and testify with clarity, presenting findings in a calm, credible manner that supports your litigation strategy.</p>
      <h2 class="section-title">Unique Investigations</h2>
      <p class="section-text">Some matters fall outside routine work. We design focused plans for unusual cases and apply the right tools to deliver answers.</p>
    </article>

    <article class="panel panel--centre">
      <h2 class="section-title">Corporate Litigation</h2>
      <p class="section-text">Our investigators assist corporate counsel with background research, asset searches and witness interviews, giving your legal team the facts needed to build a strong position.</p>
      <h2 class="section-title">Domestic</h2>
      <p class="section-text">Family matters require discretion. We handle custody, support and domestic cases with sensitivity and deliver documented findings you can rely on.</p>
      <h2 class="section-title">Locates</h2>
      <p class="section-text">We find people who do not want to be found. Using current databases and field work, we locate witnesses, defendants and heirs quickly.</p>
      <h2 class="section-title">Accident Reconstruction</h2>
      <p class="section-text">We examine scenes, gather evidence and work with experts to explain how an incident occurred.</p>
    </article>

    <article class="panel">
      <h2 class="section-title">Corporate Intelligence</h2>
      <p class="section-text">We help businesses make informed decisions through careful research on partners, competitors and key hires.</p>
      <ul class="service-list">
        <li>Due diligence reviews</li>
        <li>Background investigations</li>
        <li>Asset and lien searches</li>
        <li>Internal fraud inquiries</li>
      </ul>
    </article>
  </section>

  <section class="cover" aria-label="Brochure front panel">
    <div class="brand">
      <span class="brand__mark"></span>
      <span class="brand__name">Brenwick Inquiry Partners</span>
    </div>
    <h2 class="section-title">Attorney Services</h2>
    <p class="section-text">At Brenwick Inquiry Partners we believe our job is to make your life easier. We take on the details of each assignment so your team can focus on the case. Regardless of your firm's size, we work closely with you to reach results.</p>
    <p class="section-text">Brenwick Inquiry Partners uses the research tools you expect and the field experience you need. We offer pre and post litigation support that meets the highest standards.</p>
    <h2 class="section-title">Surveillance</h2>
    <p class="section-text">Surveillance is a core part of our work. Our investigators document activity with modern equipment, discreet methods and clear reporting, delivering video and written records that support your claims and your clients.</p>

    <ul class="contact" aria-label="Contact information">
      <li><svg viewBox="0 0 10 10" aria-hidden="true"><path d="M2 0.5 L3.8 0.5 L4.4 3 L3.2 3.9 Q4.2 6 6.1 6.8 L7 5.6 L9.5 6.2 L9.5 8 Q9.5 9.5 8 9.5 Q1 9 0.5 2 Q0.5 0.5 2 0.5 Z"/></svg>(209) 555-0148</li>
      <li><svg viewBox="0 0 10 10" aria-hidden="true"><path d="M5 0 A3.5 3.5 0 0 1 8.5 3.5 C8.5 6 5 10 5 10 C5 10 1.5 6 1.5 3.5 A3.5 3.5 0 0 1 5 0 Z M5 2.2 A1.3 1.3 0 1 0 5 4.8 A1.3 1.3 0 1 0 5 2.2 Z"/></svg>1420 Orchard Row, Suite 6, Modesto, CA</li>
      <li><svg viewBox="0 0 10 10" aria-hidden="true"><path d="M0.5 2 H9.5 V8 H0.5 Z M1.2 2.6 L5 5.4 L8.8 2.6 V3.4 L5 6.2 L1.2 3.4 Z" fill-rule="evenodd"/></svg>cases@brenwickinquiry.example</li>
    </ul>
  </section>

</main>
</body>
</html>
```